ALL TEXT Social Media Graphics

We are looking for a series of social media graphics for Instagram (new size: 4:5 (1080 x 1350 pixels) ratio that are ALL TEXT. We want the following quotes below on each graphic; one quote per graphic. AND, In very small letters at the bottom of each graphic, add @PaulaWrenLive
The look and feel of these graphics should be complimentary to the color palette attached below; but keep them simple. But the design is up to you; at the end of this document, I provided various samples of all text graphics that I like as examples.
The Quotes are in the attached WORD document
women trying to lose weight

```html
<!DOCTYPE html>
<html lang="en">
<head>
<meta charset="utf-8">
<title>Hot Girl Summer Plan</title>
<link rel="stylesheet" href="https://fonts.googleapis.com/css2?family=Anton&family=Raleway:wght@300;500;700&display=swap">
<style>
  :root {
    --pink-light: #f590b2;
    --pink-deep: #ec5c93;
    --pink-shade: #d9477f;
    --ink-white: #ffffff;
    --handle-magenta: #b0175c;
  }
  html, body {
    margin: 0;
    padding: 0;
    width: 960px;
    height: 1200px;
    overflow: hidden;
  }
  .post {
    position: relative;
    width: 960px;
    height: 1200px;
    background: linear-gradient(135deg, var(--pink-light) 0%, var(--pink-deep) 100%);
    overflow: hidden;
  }
  .post svg {
    position: absolute;
    inset: 0;
    width: 960px;
    height: 1200px;
  }
  .headline { font-family: "Anton", "Impact", sans-serif; fill: var(--ink-white); }
  .line-medium { font-family: "Raleway", sans-serif; font-weight: 500; fill: var(--ink-white); }
  .line-bold { font-family: "Raleway", sans-serif; font-weight: 700; fill: var(--ink-white); }
  .line-light { font-family: "Raleway", sans-serif; font-weight: 300; fill: var(--ink-white); }
  .handle { font-family: "Raleway", sans-serif; font-weight: 500; fill: var(--handle-magenta); }
</style>
</head>
<body>
<main class="post">
  <svg viewBox="0 0 960 1200" xmlns="http://www.w3.org/2000/svg">
    <defs>
      <radialGradient id="portraitGlow" cx="0.62" cy="0.55" r="0.6">
        <stop offset="0" stop-color="var(--pink-shade)" stop-opacity="0.45"/>
        <stop offset="1" stop-color="var(--pink-shade)" stop-opacity="0"/>
      </radialGradient>
    </defs>

    <rect class="portrait-area" x="520" y="200" width="440" height="1000"
          fill="url(#portraitGlow)" role="img"
          aria-label="Photo of a smiling woman with long dark hair in a black sheer striped top, hands on hips"/>

    <text class="headline" x="39" y="193" font-size="173" textLength="631" lengthAdjust="spacingAndGlyphs">HOT GIRL</text>
    <text class="line-medium" x="39" y="261" font-size="54" textLength="614" lengthAdjust="spacingAndGlyphs">YOU CAN ABSOLUTELY</text>
    <text class="line-bold" x="43" y="353" font-size="107" textLength="522" lengthAdjust="spacingAndGlyphs">BE DOWN</text>
    <text class="headline" x="41" y="530" font-size="175" textLength="471" lengthAdjust="spacingAndGlyphs">20–30</text>
    <text class="line-light" x="43" y="608" font-size="91" textLength="380" lengthAdjust="spacingAndGlyphs">POUNDS</text>
    <text class="line-bold" x="43" y="680" font-size="83" textLength="290" lengthAdjust="spacingAndGlyphs">BY END</text>
    <text class="line-light" x="39" y="731" font-size="50" textLength="284" lengthAdjust="spacingAndGlyphs">OF SUMMER</text>

    <text class="line-light" font-size="45">
      <tspan x="40" y="967" textLength="337" lengthAdjust="spacingAndGlyphs">ALL IT TAKES IS</tspan>
      <tspan x="40" y="1015" textLength="238" lengthAdjust="spacingAndGlyphs">THE RIGHT</tspan>
      <tspan x="40" y="1063" textLength="403" lengthAdjust="spacingAndGlyphs">PLAN—AND YOU'VE</tspan>
      <tspan x="40" y="1112" textLength="215" lengthAdjust="spacingAndGlyphs">FOUND IT</tspan>
    </text>

    <text class="handle" x="40" y="1180" font-size="30" textLength="265" lengthAdjust="spacingAndGlyphs">@PAULAWRENLIVE</text>
  </svg>
</main>
</body>
</html>
```